Clear Plastic Card Design

I am looking to have a business card designed from my logo icon. I am looking to match the style of a different business card I have attached in the files.
Looking for a card that is plastic, with layers of transparency in the shape of my logo icon (also attached in the files) - not a circle like the other card. The winning design will incorporate the red icon logo on the front and back and include the charity's name, "Lanterns for the Weary" in the same or similar font, as well as an email and phone number. For now, use the email: email@lanternsfortheweary.org and the phone number 555-318-4072.
We like how the sample business card has transparency, partial and full opacity layers and a matching color scheme. Files will need to be in vector so that our business card printing company can work with it.
UPDATE:
We've some excellent designs in, thank you everyone! I got an early review from the owner, and he requested a minor redirect to find his perfect design. He wants the design to stand out by NOT being a rectangle. Try instead a circle, square, or best yet - something that falls in the outline of the logo icon, either fully or partially. Thank you, everyone!
Contact Information for Business Card
Lanterns for the Weary text should be incorporated as well as a phone and email.
Look and feel

```html
<!DOCTYPE html>
<html lang="en">
<head>
<meta charset="utf-8">
<title>Lanterns for the Weary – Round Cards</title>
<link rel="stylesheet" href="https://fonts.googleapis.com/css2?family=Comfortaa:wght@500&family=Bebas+Neue&display=swap">
<style>
  :root {
    --page: #e9e6e3;
    --card: #333333;
    --card-rim: #262626;
    --white: #ffffff;
    --accent: #ee5a16;
    --accent-deep: #e0301e;
  }
  * { margin: 0; padding: 0; box-sizing: border-box; }
  html, body { width: 1200px; height: 800px; overflow: hidden; }
  body { background: var(--page); position: relative; }

  .card {
    position: absolute;
    width: 476px; height: 476px;
    border-radius: 50%;
    background: var(--card);
    border: 14px solid var(--card-rim);
  }
  .card--front { left: 110px; top: 206px; }
  .card--back  { left: 614px; top: 206px; }

  .brand {
    position: absolute;
    display: flex; align-items: center;
    font-family: "Comfortaa", sans-serif;
    font-weight: 500;
    color: var(--white);
    line-height: 1.1;
  }
  .brand__dot {
    flex: none;
    border-radius: 50%;
    background: var(--accent);
  }
  .brand--large { left: 58px; top: 150px; font-size: 30px; gap: 18px; }
  .brand--large .brand__dot { width: 96px; height: 96px; }
  .brand--small { left: 128px; top: 54px; font-size: 15px; gap: 10px; }
  .brand--small .brand__dot { width: 50px; height: 50px; }

  .contact {
    position: absolute; left: 36px;
    display: flex; align-items: center; gap: 14px;
    color: var(--white);
  }
  .contact--phone { top: 196px; }
  .contact--email { top: 244px; }
  .contact__icon {
    width: 40px; height: 40px;
    background: var(--accent);
    display: flex; align-items: center; justify-content: center;
  }
  .contact--phone .contact__icon { border-radius: 12px 12px 4px 4px; }
  .contact--email .contact__icon { border-radius: 4px 4px 12px 12px; }
  .contact__icon svg { width: 20px; height: 20px; }
  .contact__text { font-family: "Bebas Neue", sans-serif; }
  .contact--phone .contact__text { font-size: 36px; letter-spacing: 0.5px; }
  .contact--email .contact__text { font-size: 22px; letter-spacing: 0.6px; }

  .tagline {
    position: absolute; left: 16px; top: 298px;
    width: 416px; height: 58px;
    border-top: 2px solid var(--accent);
    border-bottom: 2px solid var(--accent);
    font-family: "Bebas Neue", sans-serif;
    font-size: 36px; letter-spacing: 0.5px;
    color: var(--accent-deep);
    display: flex; align-items: center; justify-content: center;
  }
</style>
</head>
<body>
  <section class="card card--front">
    <div class="brand brand--large">
      <span class="brand__dot"></span>
      <span class="brand__name">Lanterns for the<br>Weary</span>
    </div>
  </section>

  <section class="card card--back">
    <div class="brand brand--small">
      <span class="brand__name">Lanterns for the<br>Weary</span>
      <span class="brand__dot"></span>
    </div>

    <div class="contact contact--phone">
      <span class="contact__icon">
        <svg viewBox="0 0 24 24" aria-hidden="true"><path fill="#fff" d="M6.6 10.8a15.1 15.1 0 0 0 6.6 6.6l2.2-2.2c.3-.3.7-.4 1-.2 1.1.4 2.3.6 3.6.6.6 0 1 .4 1 1V20c0 .6-.4 1-1 1A17 17 0 0 1 3 4c0-.6.4-1 1-1h3.5c.6 0 1 .4 1 1 0 1.3.2 2.5.6 3.6.1.3 0 .7-.2 1z"/></svg>
      </span>
      <span class="contact__text">555-318-4072</span>
    </div>

    <div class="contact contact--email">
      <span class="contact__icon">
        <svg viewBox="0 0 24 24" aria-hidden="true"><rect x="3" y="5" width="18" height="14" rx="2" fill="none" stroke="#fff" stroke-width="2"/><path d="M3 7l9 6 9-6" fill="none" stroke="#fff" stroke-width="2"/></svg>
      </span>
      <span class="contact__text">EMAIL@LANTERNSFORTHEWEARY.ORG</span>
    </div>

    <div class="tagline">LANTERNS FOR THE WEARY</div>
  </section>
</body>
</html>
```